36" inch (height) x 96" inch (width) Banner for Baseball Field

Hello. This project is an advertisement that will be printed onto a 3 foot by 8 foot full color banner and placed at little league fields in Southern California. A theme of the banner can be baseball. The company is my law office practicing Estate Planning and Tax Law. I am uploading the current business card, which has the logo, website, and telephone number. You can also pull images from www.rkmorvadell.example I would like the banner to be a fun design that incorporates baseball somehow, but draws attention to my law and tax office, and my website. Please be creative, and have fun with it. The colors of my practice are included in the logo. At the bottom, it should say "Attorney Advertisement," but this can be in very small font in the bottom right or left corner.
Updates

Target Market(s)

Youth Baseball Fans

Industry/Entity Type

Law; Accounting

Colors

Designer to choose colors to be used in the design.

Requirements
Must have
• My telephone number. My website.
Nice to have
• Would like to see "Estate Planning" and "Tax Law and Preparation" Would also like to see "Attorney" and "CPA" or "Certified Public Accountant" prominently diplayed

```html
<!DOCTYPE html>
<html lang="en">
<head>
<meta charset="utf-8">
<title>RK Morvadell – Ballfield Banner</title>
<link rel="stylesheet" href="https://fonts.googleapis.com/css2?family=Saira+Condensed:wght@400;600&family=Saira:wght@300;400&display=swap">
<style>
  :root {
    --page: #ffffff;
    --ink: #000000;
    --white: #ffffff;
    --brand-blue: #1a9be0;
    --muted: #c9c9c9;
    --rail-dark: #1a1a1a;
    --rail-light: #d8d8d8;
    --field-green: #2f5a1e;
    --field-clay: #8a4a28;
  }
  html, body {
    margin: 0;
    padding: 0;
    width: 1079px;
    height: 1200px;
    overflow: hidden;
    background: var(--page);
  }
  .canvas {
    position: relative;
    width: 1079px;
    height: 1200px;
  }
  .banner-rail {
    position: absolute;
    left: 40px;
    top: 408px;
    width: 998px;
    height: 12px;
    background: linear-gradient(90deg, var(--rail-light) 0%, var(--rail-dark) 20%, var(--rail-dark) 80%, var(--rail-light) 100%);
  }
  .banner {
    position: absolute;
    left: 40px;
    top: 420px;
    width: 998px;
    height: 362px;
    background: var(--ink);
    overflow: hidden;
  }
  .stadium-photo {
    position: absolute;
    inset: 0 0 12px 0;
    background:
      linear-gradient(90deg, rgba(0,0,0,0.85) 0%, rgba(0,0,0,0.2) 35%, rgba(0,0,0,0.2) 70%, rgba(0,0,0,0.8) 100%),
      linear-gradient(180deg, #050505 0%, #141414 25%, #2a2320 45%, var(--field-green) 65%, var(--field-clay) 82%, #241a12 100%);
  }
  .accent-band {
    position: absolute;
    left: 0;
    right: 0;
    bottom: 0;
    height: 12px;
    background: var(--brand-blue);
  }
  .left-column {
    position: absolute;
    left: 22px;
    top: 0;
    width: 330px;
    height: 350px;
    text-align: center;
    font-family: "Saira", sans-serif;
    white-space: nowrap;
  }
  .left-column p {
    position: absolute;
    left: 0;
    right: 0;
    margin: 0;
  }
  .firm-mark {
    position: absolute;
    left: 119px;
    top: 24px;
  }
  .firm-intro {
    top: 121px;
    font-weight: 300;
    font-size: 14px;
    line-height: 18px;
    letter-spacing: 2px;
    color: var(--muted);
    text-transform: uppercase;
  }
  .firm-name {
    top: 142px;
    font-weight: 400;
    font-size: 32px;
    line-height: 38px;
    letter-spacing: 1px;
    color: var(--brand-blue);
    text-transform: uppercase;
  }
  .contact-web {
    top: 200px;
    font-weight: 300;
    font-size: 24px;
    line-height: 30px;
    color: var(--white);
  }
  .contact-phone {
    top: 236px;
    font-weight: 300;
    font-size: 40px;
    line-height: 48px;
    color: var(--white);
  }
  .disclaimer {
    top: 306px;
    font-weight: 400;
    font-size: 13px;
    line-height: 18px;
    color: var(--white);
  }
  .services {
    position: absolute;
    right: 33px;
    top: 26px;
    text-align: right;
    font-family: "Saira Condensed", sans-serif;
    font-weight: 600;
    font-size: 44px;
    line-height: 45px;
    color: var(--white);
    white-space: nowrap;
  }
  .services p { margin: 0; }
  .services .group + .group { margin-top: 18px; }
  .services .connector { font-weight: 400; }
  .services .highlight { color: var(--brand-blue); }
</style>
</head>
<body>
<div class="canvas">
  <div class="banner-rail"></div>
  <section class="banner">
    <div class="stadium-photo" role="img" aria-label="Night photo of a baseball stadium with players on the infield, crowd stands and scoreboard"></div>
    <div class="accent-band"></div>

    <div class="left-column">
      <svg class="firm-mark" width="92" height="92" viewBox="0 0 92 92" aria-hidden="true">
        <circle cx="46" cy="46" r="40" fill="none" stroke="var(--brand-blue)" stroke-width="6"/>
      </svg>
      <p class="firm-intro">The Law Offices of</p>
      <p class="firm-name">RK Morvadell</p>
      <p class="contact-web">www.rkmorvadell.example</p>
      <p class="contact-phone">(805) 555-0148</p>
      <p class="disclaimer">Attorney Advertisement</p>
    </div>

    <div class="services">
      <div class="group">
        <p>Estate Planning</p>
        <p><span class="connector">and</span> <span class="highlight">Tax Law and</span></p>
        <p class="highlight">Preparation</p>
      </div>
      <div class="group">
        <p>Attorney <span class="connector">and</span></p>
        <p class="highlight">Certified Public</p>
        <p class="highlight">Accountant</p>
      </div>
    </div>
  </section>
</div>
</body>
</html>
```